Bright Arch Group business card

Bright Arch Group is the parent company of Bright Arch Building, Bright Arch Plumbing and Bright Arch Renovating. We require a sophisticated business card that covers all aspects of the building and plumbing space without using told or construction items.

Industry/Entity Type

Construction Company

Contact Information for Business Card

Warrick Hadley
Director
0455921834
warrick@brightarch.com.au
Www.brightarch.com.au

Font styles to use
Serif
Sans Serif

Colors
3176b5
ffce3e
0692cd
34a7d8
fbee3e
faa54b

Requirements
Must have
• Logo on front
• Logo and details on rear.
Nice to have
• Maybe water mark or shadow effect with logo
Should not have
• Tools or any construction associated items

```html
<!DOCTYPE html>
<html lang="en">
<head>
<meta charset="utf-8">
<title>Bright Arch Group – Business Card</title>
<link rel="stylesheet" href="https://fonts.googleapis.com/css2?family=Cormorant+Garamond:wght@500;600&family=Mulish:wght@300;400;800&display=swap">
<style>
  :root {
    --backdrop: #e8e3dc;
    --card-white: #ffffff;
    --ink: #2a2a2a;
    --ink-soft: #555555;
    --accent-orange: #e8892a;
    --front-edge: #d2611c;
    --front-mid: #e5902f;
    --front-glow: #f0c33c;
    --front-text: #ffffff;
  }
  * { margin: 0; padding: 0; box-sizing: border-box; }
  html, body {
    width: 1200px;
    height: 1023px;
    overflow: hidden;
    background: var(--backdrop);
  }
  .canvas {
    position: relative;
    width: 1200px;
    height: 1023px;
  }
  .card {
    position: absolute;
    top: 361px;
    width: 525px;
    height: 300px;
    box-shadow: 0 6px 18px rgba(60, 40, 20, 0.22);
    overflow: hidden;
  }
  .card--back {
    left: 50px;
    background: var(--card-white);
  }
  .card--front {
    left: 625px;
    background: radial-gradient(ellipse 60% 70% at 55% 50%, var(--front-glow) 0%, var(--front-mid) 45%, var(--front-edge) 100%);
    display: flex;
    align-items: center;
    justify-content: center;
  }

  /* back side: person and contact details */
  .holder {
    position: absolute;
    left: 42px;
    top: 168px;
  }
  .holder__name {
    font-family: "Cormorant Garamond", serif;
    font-weight: 600;
    font-variant: small-caps;
    font-size: 27px;
    letter-spacing: 0.5px;
    color: var(--ink);
    line-height: 1;
  }
  .holder__role {
    font-family: "Mulish", sans-serif;
    font-weight: 400;
    font-size: 17px;
    color: var(--accent-orange);
    margin-top: 6px;
    margin-left: 28px;
  }
  .contact {
    position: absolute;
    left: 268px;
    top: 52px;
    font-family: "Mulish", sans-serif;
    color: var(--ink-soft);
  }
  .contact__phone {
    font-weight: 800;
    font-size: 25px;
    letter-spacing: 0.3px;
    color: #3a3a3a;
    line-height: 1.1;
  }
  .contact__line {
    font-weight: 300;
    font-size: 16px;
    letter-spacing: 0.6px;
    line-height: 1.45;
    margin-left: 22px;
  }

  /* front side: company name */
  .brand {
    font-family: "Mulish", sans-serif;
    font-weight: 300;
    color: var(--front-text);
    text-transform: uppercase;
    text-align: center;
    line-height: 1.5;
  }
  .brand__main {
    display: block;
    font-size: 36px;
    letter-spacing: 12px;
  }
  .brand__sub {
    display: block;
    font-size: 20px;
    letter-spacing: 16px;
  }
</style>
</head>
<body>
  <main class="canvas">
    <section class="card card--back" aria-label="Card reverse with contact details">
      <div class="holder">
        <p class="holder__name">Warrick Hadley</p>
        <p class="holder__role">Director</p>
      </div>
      <div class="contact">
        <p class="contact__phone">0455921834</p>
        <p class="contact__line">warrick@brightarch.com.au</p>
        <p class="contact__line">www.brightarch.com.au</p>
      </div>
    </section>

    <section class="card card--front" aria-label="Card front with company name">
      <p class="brand">
        <span class="brand__main">Bright Arch</span>
        <span class="brand__sub">Group</span>
      </p>
    </section>
  </main>
</body>
</html>
```